Designing a brochures for an educational counseling service provider

We would like a 4 sided design on a 11x8.5 paper, half folded. I have including a sample design we did to give you an idea of what we envision but we welcome creativity to make beautiful looking flyers. Text for the flier is included as well as our logo.
- The most important thing is capturing our audience/market. We will be handing these flies to schools, organizations and individual clients.

www.plorvaeducationalconsultants.example

Target Market(s)

We are targeting international students wanting to study in the U.S and Canada.

Industry/Entity Type

Education

Requirements
Must have
• - Clean and clear
• - Our logo should visible and well placed.
• - Could you the pictures of students, libraries and school buildings or you could use the pictures we already have.
Nice to have
• We would like this to match business cards.

```html
<!DOCTYPE html>
<html lang="en">
<head>
<meta charset="utf-8">
<title>Plorva Educational Consultants – Brochure</title>
<link rel="stylesheet" href="https://fonts.googleapis.com/css2?family=Montserrat:wght@600;700;800&family=Open+Sans:ital,wght@0,400;0,600;0,700;1,400&display=swap">
<style>
:root{
  --navy:#1d3c8c;
  --navy-deep:#142c6b;
  --orange:#f26a1f;
  --ink:#2b2f3a;
  --muted:#5a6272;
  --paper:#ffffff;
  --mist:#eef2f8;
  --stage:#e4e7ec;
}
*{box-sizing:border-box;margin:0;padding:0}
html,body{width:880px;height:1200px;overflow:hidden}
body{background:var(--stage);font-family:"Open Sans",Arial,sans-serif;color:var(--ink);position:relative}
.spread{position:absolute;left:0;width:880px;height:560px;background:var(--paper);display:flex;box-shadow:0 2px 6px rgba(0,0,0,.15)}
.spread--outside{top:20px}
.spread--inside{top:620px}
.panel{position:relative;width:440px;height:560px;overflow:hidden}
.panel + .panel{border-left:1px solid #d7dce5}
.photo{position:absolute}
.head{font-family:"Montserrat",Arial,sans-serif;font-weight:800;text-transform:uppercase;line-height:1.15}
.orange{color:var(--orange)}
.navy{color:var(--navy)}

/* back panel */
.back .brand-head{position:absolute;left:22px;top:18px}
.back .brand-head .head{font-size:15px}
.back .brand-head .head.navy{font-size:16.5px}
.back .photo{left:0;top:70px;width:440px;height:230px;background:linear-gradient(135deg,#c9b497,#7d6a56 55%,#3f3a3d)}
.mission{position:absolute;left:0;top:300px;width:440px;height:78px;background:var(--navy);padding:16px 22px;color:var(--orange);font-family:"Montserrat",Arial,sans-serif;font-weight:700;font-size:13px;line-height:1.35}
.contact{position:absolute;left:22px;top:392px;width:396px}
.contact h3{font-family:"Montserrat",Arial,sans-serif;font-weight:800;font-size:16px;color:var(--orange);margin-bottom:8px}
.contact .cols{display:flex;gap:24px;font-size:10px;line-height:1.6;color:var(--muted)}
.contact .cols div{flex:1}
.contact .row{display:flex;align-items:center;gap:6px}
.contact svg{flex:none}
.web{position:absolute;left:0;bottom:14px;width:100%;text-align:center;font-weight:700;font-size:11px;color:var(--orange)}

/* cover panel */
.cover .logo{position:absolute;right:24px;top:18px;display:flex;align-items:center;gap:10px}
.cover .logo .mark{width:38px;height:38px;border-radius:50%;background:var(--navy)}
.cover .logo span{font-family:"Montserrat",Arial,sans-serif;font-weight:800;font-size:17px;color:var(--navy);line-height:1.1;width:150px}
.cover .photo{left:0;top:78px;width:440px;height:250px;background:linear-gradient(160deg,#8fb3d9,#3d5f8e 50%,#2a2d3a)}
.tagline{position:absolute;left:0;top:300px;width:440px;height:88px;background:var(--navy);padding:18px 24px 0 170px;color:#fff;font-family:"Montserrat",Arial,sans-serif;font-weight:700;font-size:13.5px;line-height:1.35}
.tagline::before{content:"";position:absolute;left:0;top:0;width:150px;height:88px;background:var(--orange)}
.icons{position:absolute;left:16px;top:404px;width:408px;display:flex;justify-content:space-between}
.icon{width:96px;text-align:center;font-size:10px;font-weight:700;color:var(--navy);line-height:1.25}
.icon .disc{width:46px;height:46px;border-radius:50%;background:var(--orange);margin:0 auto 6px;display:flex;align-items:center;justify-content:center}

/* inside */
.tab{position:absolute;left:0;top:16px;height:36px;display:flex;align-items:center}
.tab .label{background:var(--orange);color:#fff;font-family:"Montserrat",Arial,sans-serif;font-weight:800;font-size:17px;padding:0 16px;height:36px;line-height:36px}
.tab .names{padding-left:12px;font-size:9px}
.tab .names .head{font-size:10px}
.about .photo{left:0;top:62px;width:440px;height:168px;background:linear-gradient(180deg,#b7c6d8,#6c7d93 60%,#3c4353)}
.quote{position:absolute;left:0;top:230px;width:440px;height:66px;background:var(--navy);padding:12px 22px;color:#fff;font-style:italic;font-size:11px;line-height:1.4}
.quote b{display:block;text-align:right;font-style:normal;font-family:"Montserrat",Arial,sans-serif;font-size:10px;color:var(--orange)}
.about .body{position:absolute;left:22px;top:306px;width:396px;font-size:9px;line-height:1.5;color:var(--muted)}
.about .body p+p{margin-top:5px}
.bar{background:var(--orange);color:#fff;font-family:"Montserrat",Arial,sans-serif;font-weight:700;font-size:10.5px;padding:3px 10px}
.about .bar{position:absolute;left:22px;top:420px;width:396px}
.list{position:absolute;left:22px;top:446px;width:396px;columns:2;column-gap:20px;font-size:9.5px;line-height:1.75;list-style:none;color:var(--ink)}
.list li::before{content:"•";color:var(--orange);margin-right:6px}

.services{background:var(--mist)}
.services .body{position:absolute;left:22px;top:64px;width:396px}
.service{margin-bottom:11px}
.service .bar{display:inline-block;margin-bottom:5px}
.service p{font-size:9px;line-height:1.5;color:var(--muted)}
.service p+p{margin-top:4px}
</style>
</head>
<body>

<section class="spread spread--outside">
  <article class="panel back">
    <div class="brand-head">
      <div class="head orange">Plorva Educational Consultants</div>
      <div class="head navy">International Students Solutions</div>
    </div>
    <div class="photo" role="img" aria-label="Photo of students reading in a library"></div>
    <div class="mission">Our mission is to make global educational experiences affordable and accessible to the families we serve.</div>
    <div class="contact">
      <h3>CONTACT US</h3>
      <div class="cols">
        <div>
          <div class="row"><svg width="10" height="12" viewBox="0 0 10 12"><path d="M5 0a4 4 0 0 0-4 4c0 3 4 8 4 8s4-5 4-8a4 4 0 0 0-4-4z" fill="#f26a1f"/><circle cx="5" cy="4" r="1.5" fill="#fff"/></svg>2240 Harlow Ave, Suite 310</div>
          <div class="row" style="padding-left:16px">Columbus, OH 43200</div>
          <div class="row"><svg width="10" height="10" viewBox="0 0 10 10"><path d="M2 0l2 2-1 2c1 1 2 2 3 3l2-1 2 2-2 2C4 10 0 6 0 2z" fill="#f26a1f"/></svg>614-555-0148</div>
          <div class="row"><svg width="10" height="8" viewBox="0 0 10 8"><rect width="10" height="8" fill="#f26a1f"/><path d="M0 0l5 4 5-4" stroke="#fff" fill="none"/></svg>hello@plorva.example</div>
        </div>
        <div>
          <strong style="color:var(--navy)">Maren Holt</strong><br>
          Executive Director &amp; Independent Educational Consultant<br>
          Member, International Education Association
        </div>
      </div>
    </div>
    <div class="web">www.plorvaeducationalconsultants.example</div>
  </article>

  <article class="panel cover">
    <div class="logo"><div class="mark"></div><span>Plorva Educational Consultants</span></div>
    <div class="photo" role="img" aria-label="Photo of a smiling group of international students"></div>
    <div class="tagline">A full-service international educational consulting group serving students and families across the globe.</div>
    <div class="icons">
      <div class="icon"><div class="disc"><svg width="24" height="22" viewBox="0 0 24 22"><path d="M12 2L2 8h20zM4 9h3v9H4zm6 0h4v9h-4zm7 0h3v9h-3zM2 19h20v2H2z" fill="#fff"/></svg></div>Boarding<br>Schools</div>
      <div class="icon"><div class="disc"><svg width="26" height="18" viewBox="0 0 26 18"><path d="M13 0L0 6l13 6 13-6zM5 9v5c4 4 12 4 16 0V9l-8 4z" fill="#fff"/></svg></div>College<br>Admission</div>
      <div class="icon"><div class="disc"><svg width="24" height="18" viewBox="0 0 24 18"><path d="M2 5h14V1l6 6-6 6V9H2zM22 13H8v-3l-6 5 6 3v-3h14z" fill="#fff"/></svg></div>Transfer<br>Students</div>
      <div class="icon"><div class="disc"><svg width="22" height="22" viewBox="0 0 22 22"><circle cx="11" cy="7" r="5" fill="#fff"/><path d="M2 21c0-5 4-8 9-8s9 3 9 8z" fill="#fff"/></svg></div>Graduate<br>Students</div>
    </div>
    <div class="web">www.plorvaeducationalconsultants.example</div>
  </article>
</section>

<section class="spread spread--inside">
  <article class="panel about">
    <div class="tab"><div class="label">ABOUT US:</div><div class="names"><div class="head orange">Plorva Educational Consultants</div><div class="head navy">International Students Solutions</div></div></div>
    <div class="photo" role="img" aria-label="Photo of a university library hall"></div>
    <div class="quote">“Plorva made our college search easy and we got into our number one choice school.”<b>– DANIEL ORTIZ</b></div>
    <div class="body">
      <p>Our team is a warm, caring and highly experienced group of advisors who guide students from many countries toward schools in the United States and Canada. We listen first, then build a plan that fits each learner's goals, budget and timeline.</p>
      <p>Finding the right school is important. Our staff visits campuses every year and keeps close ties with admissions offices, so families receive current, honest advice at every step of the process.</p>
    </div>
    <div class="bar">Our services include:</div>
    <ul class="list">
      <li>School selection</li>
      <li>Campus visit planning</li>
      <li>Application support</li>
      <li>Essay review and coaching</li>
      <li>Interview preparation</li>
      <li>Visa and document guidance</li>
      <li>Scholarship search</li>
      <li>Arrival and settling support</li>
    </ul>
  </article>

  <article class="panel services">
    <div class="tab"><div class="label">SERVICES:</div><div class="names"><div class="head orange">Plorva Educational Consultants</div><div class="head navy">International Students Solutions</div></div></div>
    <div class="body">
      <div class="service"><span class="bar">Boarding schools</span>
        <p>We help families find boarding schools that offer strong academics, a safe home and a supportive community. Our advisors compare programs, arrange visits and guide students through testing and applications.</p>
        <p>Each plan is shaped around the student's interests, learning style and long-term goals.</p></div>
      <div class="service"><span class="bar">College admission</span>
        <p>From building a school list to polishing essays, we walk students through every stage of college admission. We explain deadlines, testing and financial aid so families can choose with confidence.</p>
        <p>Our goal is a strong match between student and campus, not only an offer letter.</p></div>
      <div class="service"><span class="bar">Transfer students</span>
        <p>Students who wish to move to a new college receive clear advice on credit transfer, timing and applications, helping them continue their studies without losing progress.</p></div>
      <div class="service"><span class="bar">Scholarships</span>
        <p>We search for merit and need-based awards open to international students and help prepare strong applications that highlight each student's achievements.</p>
        <p>Many of our students receive aid that makes study abroad far more affordable.</p></div>
    </div>
  </article>
</section>

</body>
</html>
```